素人ながらに一応簡単に自分で作成しました

今回はコロナの為、葬儀を簡潔に済ませる方が増えてきており(蜜を避ける)
火葬式メインのチラシを考えております。
とはいえ、家族葬と比較しているお客様にも他のプランもあることを
告知はしたいと思います。
(コロナ対策として、検温実施・お席の間隔を空ける・アルコール除菌・受付所の飛沫感染ボード用意等)

内容(項目や金額)を参考にしていただきレイアウトや色使いその他画像
をデザイナーさん目線でお願いいたします。

皆様の提案を見て、更ににあれこれ入れてほしいと要望が出るかもしれませんがよろしくお願いいたします。

記載項目
【社名】アオイ葬祭
【住所】さいたま市緑区上小池412-5
【電話】フリーダイヤル 0120-53-1046
【ロゴ】添付いたします
【チラシ限定】【さいたま市限定】【市内最安値】
青系、水色系、緑系、紫系
一応自分で簡単に作成しました内容を参考にしてください
(金額・プラン項目当)

はるきち様

今回は素敵なご提案本当にありがとうございます。
弊社女性スタッフの推薦が1番多かったです。
後ほど多少の修正依頼をお願いしたいと思います。

引き続き宜しくお願い致します。

今回は皆さまとても素敵なご提案ありがとうございました。

皆さまそれぞれ良い所があり中々決められずにギリギリになってしまい申し訳ありませんでした。

コロナが落ち着きましたら、通常プランでのチラシも考えておりますので
また宜しくお願いしたいと思います。

今回は本当にありがとうございました。

```html
<!DOCTYPE html>
<html lang="ja">
<head>
<meta charset="utf-8">
<title>アオイ葬祭 火葬式・花葬式 チラシ</title>
<link href="https://fonts.googleapis.com/css2?family=Noto+Sans+JP:wght@400;500;700&family=Noto+Serif+JP:wght@500;700;900&display=swap" rel="stylesheet">
<style>
:root{
  --navy:#1d2f5c;
  --blue:#2f5fa8;
  --sky:#8ec7ea;
  --purple:#7a4c9c;
  --violet:#b693d2;
  --lav:#ece6f3;
  --ink:#33364a;
  --white:#ffffff;
  --gold:#e7d48a;
  --row:#f3f4f8;
  --rose:#c2456b;
}
*{margin:0;padding:0;box-sizing:border-box}
html,body{width:848px;height:1200px;overflow:hidden;background:var(--white)}
body{font-family:"Noto Sans JP",sans-serif;color:var(--ink)}
.flyer{position:relative;width:848px;height:1200px;background:linear-gradient(180deg,#fff 0,#fff 70px,#f1eef7 70px,#e9eef7 420px,#fff 440px)}
.brand{position:absolute;left:24px;top:18px;display:flex;align-items:center;gap:10px;font-family:"Noto Serif JP",serif;font-weight:700;font-size:24px;color:var(--blue)}
.brand-dot{width:22px;height:22px;border-radius:50%;background:var(--purple)}
.limit-tag{position:absolute;right:28px;top:0;width:96px;height:64px;background:var(--navy);color:var(--white);font-weight:700;font-size:15px;text-align:center;line-height:1.35;padding-top:12px}
.lead{position:absolute;left:0;right:0;top:78px;text-align:center;font-family:"Noto Serif JP",serif;font-weight:700;font-size:36px;color:var(--navy);letter-spacing:4px}
.plans{position:absolute;left:20px;right:20px;top:150px;display:flex;gap:4px}
.plan{flex:1;height:270px;color:var(--white);text-align:center;padding-top:22px}
.plan--cremation{background:linear-gradient(160deg,#6fa9dd,#2a4f95 70%,#1d2f5c)}
.plan--flower{background:linear-gradient(200deg,#c7a4df,#8a5aae 60%,#5e3a82)}
.plan-tag{font-family:"Noto Serif JP",serif;font-weight:500;font-size:19px;line-height:1.5}
.plan-name{font-family:"Noto Serif JP",serif;font-weight:900;font-size:74px;line-height:1.25;letter-spacing:4px;margin-top:6px}
.plan-price{font-family:"Noto Serif JP",serif;font-weight:900;font-size:64px;color:var(--gold);line-height:1.1}
.plan-price small{font-size:36px}
.plan-price sub{font-size:11px;vertical-align:top;color:var(--white)}
.about{position:absolute;left:20px;right:20px;top:424px;height:210px;display:flex;gap:4px}
.about-box{flex:1;padding:16px 20px;color:var(--white);font-size:12px;line-height:1.7}
.about-box--cremation{background:var(--navy)}
.about-box--flower{background:#4b2f6b}
.about-title{font-family:"Noto Serif JP",serif;font-size:17px;font-weight:700;color:var(--gold);margin-bottom:8px}
.flower-row{display:flex;gap:10px}
.flower-photo{width:150px;height:96px;background:linear-gradient(135deg,#f4d9e8,#e9b6cf 50%,#a8c98f);flex:none}
.flower-note{font-size:11px;margin-top:10px}
.items{position:absolute;left:20px;right:20px;top:646px}
.items-head{text-align:center;background:var(--lav);color:var(--navy);font-weight:700;font-size:16px;padding:6px 0;margin-bottom:4px}
.items-table{width:100%;border-collapse:separate;border-spacing:0 3px;font-size:13px}
.items-table td{height:28px;text-align:center;background:var(--row)}
.items-table td.label{width:150px;background:var(--navy);color:var(--white);font-weight:700;letter-spacing:2px}
.items-table td.empty{background:#e7e8ee;color:#999}
.options{position:absolute;left:20px;right:20px;top:975px;display:flex;font-size:12px;background:var(--row)}
.options-label{background:var(--navy);color:var(--white);padding:6px 12px;font-weight:700}
.options-list{padding:6px 12px;color:var(--ink)}
.safety{position:absolute;left:20px;right:20px;top:1016px;text-align:center;font-size:11.5px;color:var(--rose);font-weight:500;border-top:1px solid #e3dcea;border-bottom:1px solid #e3dcea;padding:5px 0}
.contact{position:absolute;left:20px;right:20px;top:1050px;height:92px;display:flex;align-items:center;background:linear-gradient(90deg,var(--navy),#3b2f66);color:var(--white);padding:0 24px;gap:24px}
.contact-name{font-family:"Noto Serif JP",serif;font-weight:700;font-size:24px;display:flex;align-items:center;gap:8px}
.contact-name .brand-dot{width:16px;height:16px;background:var(--violet)}
.contact-addr{font-size:12px;margin-top:4px;opacity:.9}
.contact-tel{margin-left:auto;text-align:right}
.contact-tel-label{font-size:12px;color:var(--gold)}
.contact-tel-num{display:flex;align-items:center;gap:8px;font-family:"Noto Serif JP",serif;font-weight:900;font-size:36px;line-height:1.1;letter-spacing:1px}
.contact-tel-num svg{width:28px;height:28px}
.footnote{position:absolute;left:0;right:0;top:1158px;text-align:center;font-size:13px;color:var(--navy)}
</style>
</head>
<body>
<div class="flyer">
  <div class="brand"><span class="brand-dot"></span>アオイ葬祭</div>
  <div class="limit-tag">さいたま市民<br>限定</div>

  <h1 class="lead">感謝の気持を込めて…</h1>

  <div class="plans">
    <section class="plan plan--cremation">
      <p class="plan-tag">ご予算抑え、<br>しめやかに故人を送りたい</p>
      <h2 class="plan-name">火葬式</h2>
      <p class="plan-price">75,000<small>円</small><sub>(税別)</sub></p>
    </section>
    <section class="plan plan--flower">
      <p class="plan-tag">華やかに、<br>最期は家族で送りたい</p>
      <h2 class="plan-name">花葬式</h2>
      <p class="plan-price">98,000<small>円</small><sub>(税別)</sub></p>
    </section>
  </div>

  <div class="about">
    <div class="about-box about-box--cremation">
      <h3 class="about-title">火葬式とは</h3>
      <p>火葬式はお通夜や告別式を行わず、おだやかに故人様をお見送りするご葬儀です。ご遺体をご安置し、近親者のみで火葬場へ向かいます。費用を抑えてご家族中心に心を込めてお送りいただけます。</p>
    </div>
    <div class="about-box about-box--flower">
      <h3 class="about-title">ご納棺花</h3>
      <div class="flower-row">
        <p>季節のお花でお棺を彩ります。ゆっくりと最期の時を過ごし、故人様を花で包みお見送りいただけます。</p>
        <div class="flower-photo" role="img" aria-label="お棺を彩る生花の写真"></div>
      </div>
      <p class="flower-note">●お花例：1〜2名／2〜3名／5〜6名</p>
    </div>
  </div>

  <div class="items">
    <div class="items-head">ご予算に含まれる項目</div>
    <table class="items-table">
      <tr><td>10km迄(病院→安置所)</td><td class="label">ご遺体搬送</td><td>10km迄(病院→安置所)</td></tr>
      <tr><td>20km迄(安置所→火葬場)</td><td class="label">寝台車</td><td>20km迄(安置所→火葬場)</td></tr>
      <tr><td>一式(高級布張り棺)</td><td class="label">棺</td><td>一式(高級布張り棺)</td></tr>
      <tr><td>骨壺・骨箱(一般的な仕様)</td><td class="label">骨壺</td><td>骨壺・骨箱(一般的な仕様)</td></tr>
      <tr><td>役所・火葬場のお手続き</td><td class="label">手続き</td><td>役所・火葬場のお手続き</td></tr>
      <tr><td>1日分</td><td class="label">ドライアイス</td><td>1日分</td></tr>
      <tr><td class="empty">―</td><td class="label">安置施設</td><td>1日分(弊社指定場所)</td></tr>
      <tr><td class="empty">―</td><td class="label">お花</td><td>生花(お棺用)</td></tr>
      <tr><td class="empty">―</td><td class="label">祭壇</td><td>祭壇(生花祭壇)</td></tr>
    </table>
  </div>

  <div class="options">
    <span class="options-label">その他オプションもご用意しております。</span>
    <span class="options-list">●遺影写真 ●会葬礼状 ●お料理 ●返礼品 ●供花・供物</span>
  </div>

  <p class="safety">【コロナ対策】●検温実施 ●お席の間隔を空ける ●アルコール除菌 ●受付所に飛沫感染防止ボード設置</p>

  <div class="contact">
    <div>
      <div class="contact-name"><span class="brand-dot"></span>アオイ葬祭</div>
      <p class="contact-addr">〒 さいたま市緑区上小池412-5</p>
    </div>
    <div class="contact-tel">
      <p class="contact-tel-label">ご相談・お見積り 24時間受付 フリーダイヤル</p>
      <p class="contact-tel-num">
        <svg viewBox="0 0 24 24" aria-hidden="true"><path fill="#e7d48a" d="M6.6 10.8a15.1 15.1 0 0 0 6.6 6.6l2.2-2.2a1 1 0 0 1 1-.25 11.4 11.4 0 0 0 3.6.57 1 1 0 0 1 1 1V20a1 1 0 0 1-1 1A17 17 0 0 1 3 4a1 1 0 0 1 1-1h3.5a1 1 0 0 1 1 1c0 1.25.2 2.45.57 3.57a1 1 0 0 1-.25 1z"/></svg>
        0120-53-1046
      </p>
    </div>
  </div>

  <p class="footnote">このチラシ限定のプランとなります。事前のご相談でお見積もり致します。</p>
</div>
</body>
</html>
```